Settings Menu Design

Need new conceptual designs for App Settings screen. Screen is to be used on Ombrelo device. Simple UX right now is great. Please see rough layouts attached.
Updates

Just want to thank everyone for submitting and working on this. Very appreciative as it's helped push the direction a little further for new revisions.

Target Market(s)

Business owners

Industry/Entity Type

Ombrelo

Font styles to use
Sans Serif

Colors
85cae6
3276b5
33b8a4
fbfbfb
dbdbdb
aaaaaa

Requirements
Must have
• Need new conceptual designs for App Settings screen. App screen will need the following:
• 4 main buttons at the top of the screen. Should include an exit button at the top:
• 1) Main Settings screen - when the user comes to settings home the following are visible: Brightness and Volume need to be interactive to adjust. Battery % needs to be visible. Versioning needs to be visible on-screen as well.
• 2) Network Settings - This has an additional 4 buttons to highlight:
• 1 - A Refresh button. A Column for IP address for a user to interact with and select. Show selected network with an icon. Maybe a star?
• 2 - Wifi Advance - settings to show: Country Code drop down button, SSID section to enter info. Security selection: None, Active. And check box or equivalent to Advanced Options button.
• 3 - Address of device: Ethternet info: _____, Wi-Fi: _____, Tablet: _____
• 4 - QR Code scanner. Tablet will activate front facing the camera and show a live image of what's in front. Needs to read: "Please hold your QR Code in front of me." - Show window of image and section for Country Code drop-down menu.
• 3) Update Applications Section - Showing latest configs and updates with the size of the update. i.e. Prism Loader (0.0.1, 809 mb) - then show item installed, indicated by a checkmark.
• 4) Advanced Settings Screen - Select language ( could be a drop-down menu), Select TimeZone, a button for Usage Feedback, Turn off button, Reboot button, password section that is editable.
• Looking for Clean, flat shaped UI design. Soft drop shadows okay.
• Layout: 1280x800
Should not have
• No beveled or embossed edges. No gloss or glass looking buttons.

```html
<!DOCTYPE html>
<html lang="en">
<head>
<meta charset="utf-8">
<title>Conceptual — Settings Home</title>
<link rel="stylesheet" href="https://fonts.googleapis.com/css2?family=Arimo:wght@700&family=Roboto:wght@300;500&display=swap">
<style>
  :root {
    --screen-bg: #26b8a3;
    --ink-white: #fbfbfb;
    --brand-blue: #3276b5;
    --sky-blue: #85cae6;
    --accent-green: #33b8a4;
    --soft-grey: #dbdbdb;
    --mid-grey: #aaaaaa;
  }
  html, body {
    margin: 0;
    padding: 0;
    width: 1200px;
    height: 750px;
    overflow: hidden;
    background: var(--screen-bg);
  }
  .screen {
    position: relative;
    width: 1200px;
    height: 750px;
    background: var(--screen-bg);
    color: var(--ink-white);
    font-family: "Roboto", Arial, sans-serif;
  }
  .status-bar {
    position: absolute;
    top: 4px;
    right: 12px;
    height: 18px;
    display: flex;
    align-items: center;
    gap: 5px;
  }
  .status-time {
    font-weight: 500;
    font-size: 12px;
    margin-left: 3px;
  }
  .app-title {
    position: absolute;
    top: 101px;
    left: 0;
    width: 100%;
    margin: 0;
    text-align: center;
    font-family: "Arimo", Arial, sans-serif;
    font-weight: 700;
    font-size: 57px;
    letter-spacing: -1px;
    line-height: 1;
  }
  .settings-menu {
    position: absolute;
    top: 334px;
    left: 0;
    width: 100%;
    margin: 0;
    padding: 0;
    list-style: none;
  }
  .menu-item {
    position: absolute;
    top: 0;
    width: 200px;
    margin-left: -100px;
    text-align: center;
  }
  .menu-item--my { left: 269px; }
  .menu-item--network { left: 488px; }
  .menu-item--update { left: 707px; }
  .menu-item--advanced { left: 926px; }
  .menu-badge {
    display: block;
    width: 128px;
    height: 128px;
    margin: 0 auto;
    box-sizing: border-box;
    border: 6.5px solid var(--ink-white);
    border-radius: 50%;
    overflow: hidden;
  }
  .badge--my { background: var(--brand-blue); }
  .badge--network { background: radial-gradient(circle at 40% 40%, var(--accent-green) 0%, var(--brand-blue) 62%); }
  .badge--update { background: radial-gradient(circle at 50% 45%, var(--ink-white) 0%, var(--sky-blue) 30%, var(--brand-blue) 62%); }
  .badge--advanced { background: linear-gradient(135deg, var(--brand-blue) 0%, var(--mid-grey) 70%, var(--soft-grey) 100%); }
  .menu-label {
    display: block;
    margin-top: 23px;
    font-weight: 300;
    font-size: 16px;
    letter-spacing: 0.1px;
  }
  .nav-bar {
    position: absolute;
    bottom: 21px;
    left: 0;
    width: 100%;
    height: 48px;
  }
  .nav-bar svg { position: absolute; top: 0; left: 0; }
</style>
</head>
<body>
<main class="screen">
  <div class="status-bar" aria-label="Status">
    <svg width="16" height="13" viewBox="0 0 16 13" aria-hidden="true"><path d="M8 12.5 0.2 3.2A12 12 0 0 1 15.8 3.2Z" fill="var(--ink-white)"/></svg>
    <svg width="13" height="13" viewBox="0 0 13 13" aria-hidden="true"><path d="M13 0V13H0Z" fill="var(--ink-white)"/></svg>
    <svg width="8" height="13" viewBox="0 0 8 13" aria-hidden="true"><rect x="0" y="1.5" width="8" height="11.5" fill="var(--ink-white)"/><rect x="2.5" y="0" width="3" height="2" fill="var(--ink-white)"/></svg>
    <span class="status-time">12:30</span>
  </div>

  <h1 class="app-title">Conceptual</h1>

  <ul class="settings-menu">
    <li class="menu-item menu-item--my">
      <span class="menu-badge badge--my" role="img" aria-label="Smiling face icon for personal settings"></span>
      <span class="menu-label">My Settings</span>
    </li>
    <li class="menu-item menu-item--network">
      <span class="menu-badge badge--network" role="img" aria-label="Globe illustration for network settings"></span>
      <span class="menu-label">Network Settings</span>
    </li>
    <li class="menu-item menu-item--update">
      <span class="menu-badge badge--update" role="img" aria-label="Cloud download illustration for application updates"></span>
      <span class="menu-label">Update Applications</span>
    </li>
    <li class="menu-item menu-item--advanced">
      <span class="menu-badge badge--advanced" role="img" aria-label="Gears illustration for advanced settings"></span>
      <span class="menu-label">Advanced Settings</span>
    </li>
  </ul>

  <nav class="nav-bar" aria-label="System navigation">
    <svg width="1200" height="48" viewBox="0 0 1200 48" aria-hidden="true">
      <g fill="none" stroke="var(--ink-white)" stroke-width="1.6">
        <path d="M512 14.5 500 21 512 27.5Z" stroke-linejoin="round"/>
        <circle cx="600" cy="21" r="6.5"/>
        <rect x="688.5" y="14.5" width="13" height="13"/>
      </g>
    </svg>
  </nav>
</main>
</body>
</html>
```